Larkin Ridge Provisions Co Website Creation

We need a website designed that goes along with our western/cattle brand vibe that our logo has. We are going to need a couple different pages including: About Us, Meat Boxes, Recipes, Contact Us.

We are going to need a shop so that people may visit the website and order meat boxes to be shipped or delivered at their home. Our mission is to provide the highest quality meat that every family can afford.

Would love to see the website design with lots of mountain range backgrounds and create a feel of open range beef that has a tradition of providing great beef. Family owned business that has been raising cattle for over 30 years.

Love the colors of using dark greens, browns, Tans, Blacks

```html
<!DOCTYPE html>
<html lang="en">
<head>
<meta charset="utf-8">
<title>Larkin Ridge Provisions Co</title>
<link rel="stylesheet" href="https://fonts.googleapis.com/css2?family=Oswald:wght@500;600;700&family=Open+Sans:wght@400;600&display=swap">
<style>
:root{
  --rust:#7a2e0c;
  --dark:#4a1905;
  --deep:#1f0d05;
  --tan:#d9a766;
  --nav:#e0963f;
  --ink:#1e1e1e;
  --white:#ffffff;
  --meat:#a8232f;
  --meat-dark:#6e1620;
}
*{box-sizing:border-box;margin:0;padding:0}
html,body{width:1200px;height:4082px;overflow:hidden}
body{position:relative;background:var(--white);font-family:"Open Sans",Arial,sans-serif;color:var(--ink)}
.abs{position:absolute}
.display{font-family:"Oswald",Impact,sans-serif;font-weight:600;text-transform:uppercase;letter-spacing:.5px}
.btn{position:absolute;background:var(--tan);color:var(--white);font-weight:600;font-size:21px;display:flex;align-items:center;justify-content:center;border-radius:6px}

.site-header{top:0;left:0;width:1200px;height:100px;background:var(--white)}
.brand{left:63px;top:16px;color:var(--dark);font-family:"Oswald",sans-serif;font-weight:600;font-size:28px;line-height:32px;text-align:center;text-transform:uppercase}
.nav{top:40px;left:480px}
.nav a{position:absolute;white-space:nowrap;color:var(--ink);text-decoration:none;font-size:17px}
.nav a.active{color:var(--nav)}
.icon-ring{width:27px;height:27px;border:2px solid var(--rust);border-radius:50%;top:38px}

.hero{top:100px;left:0;width:1200px;height:526px;background:linear-gradient(100deg,#231712 0%,#3b2218 35%,#7a2324 55%,#5a2a20 70%,#2a1a14 100%)}
.hero-title{left:63px;top:200px;color:var(--white);font-size:72px;line-height:76px;text-transform:none;font-weight:600}
.hero-text{left:66px;top:372px;width:470px;color:var(--white);font-size:15.5px;line-height:21px}
.dots{display:flex;gap:16px}
.dots span{width:9px;height:9px;border-radius:50%;background:var(--white)}
.dots span.on{background:var(--tan)}

.about-block{left:951px;top:618px;width:249px;height:470px;background:var(--dark);border-radius:40px 0 0 30px}
.about-ring{left:668px;top:840px;width:260px;height:260px;border-radius:50%;background:var(--tan)}
.about-ring-2{left:667px;top:865px;width:150px;height:150px;border-radius:50%;background:#9b3a10}
.about-card{left:705px;top:666px;width:433px;height:405px;background:var(--white);border-radius:30px;padding:26px}
.about-card .ph{width:100%;height:100%;border-radius:20px;background:radial-gradient(ellipse 55% 50% at 50% 52%,#c0384a 0%,#a8232f 45%,#d88a90 70%,#ffffff 90%)}
.section-title{color:var(--rust);font-size:42px}
.about-sub{left:63px;top:733px;width:520px;font-size:32px;line-height:42px}
.about-text{left:63px;top:830px;width:500px;font-size:15.5px;line-height:21px}

.offer-box{left:63px;top:1211px;width:297px;height:258px;background:var(--dark);border-radius:6px;color:var(--white);padding:18px}
.offer-row{display:flex;justify-content:space-between;font-size:21px;line-height:43px}
.offer-row i{font-style:normal;letter-spacing:-1px;flex:1;text-align:center}
.badge{left:470px;top:1300px;width:132px;height:132px;border-radius:50%;background:var(--rust);color:var(--white);text-align:center;padding-top:38px}
.cow{left:694px;top:1244px;width:446px;height:246px;border-radius:50% 45% 30% 40% / 45% 45% 30% 30%;background:radial-gradient(ellipse 60% 55% at 55% 40%,#8e3612 0%,#7a2e0c 55%,rgba(122,46,12,.35) 85%,rgba(255,255,255,0) 100%)}

.boxes-band{top:1490px;left:0;width:1200px;height:556px}
.circle-img{width:218px;height:218px;border-radius:50%;border:4px solid var(--white)}
.label-light{color:var(--white);font-size:26px;text-align:center;width:260px}

.step{width:168px;height:168px;border-radius:50%;background:var(--tan);display:flex;align-items:center;justify-content:center}
.step.outline{background:var(--white);border:6px solid var(--tan)}
.step-label{font-size:20px;font-weight:600;text-align:center;width:200px}

.recipe{width:224px;height:224px;border-radius:50%;border:4px solid var(--rust);overflow:hidden}
.recipe .ph{width:100%;height:100%}
.recipe-label{font-size:20px;font-weight:600;letter-spacing:1.2px;text-align:center;width:260px;line-height:20px}

.contact-bg{top:3218px;left:0;width:1200px;height:500px;background:linear-gradient(180deg,#6f8f9e 0%,#35522a 22%,#3f6b2a 40%,#5f9a2e 70%,#4f8a24 100%)}
.contact-card{left:281px;top:3260px;width:635px;height:438px;background:var(--dark);border-radius:22px}
.field{position:absolute;background:var(--white);border-radius:4px;font-size:15px;padding:10px 18px;color:#333}

.footer{top:3717px;left:0;width:1200px;height:365px;background:var(--deep);overflow:hidden}
.foot-h{color:var(--nav);font-size:22px;font-weight:600}
.foot-link{color:var(--white);font-size:18px}
.copy{left:0;top:4040px;width:1200px;height:42px;background:#2e1709;color:#d9c7b3;font-size:11px;text-align:center;padding-top:16px}
</style>
</head>
<body>

<header class="site-header abs">
  <div class="brand abs">Larkin Ridge<br>Provisions Co</div>
  <nav class="nav abs">
    <a class="active" style="left:1px">Home</a>
    <a style="left:88px">About Us</a>
    <a style="left:208px">Meat Boxes</a>
    <a style="left:354px">Recipes</a>
    <a style="left:458px">Contact Us</a>
  </nav>
  <div class="icon-ring abs" style="left:1071px"></div>
  <div class="icon-ring abs" style="left:1108px"></div>
</header>

<section class="hero abs" role="img" aria-label="Raw steaks on a wooden board with a knife, pepper and tomatoes on a dark table"></section>
<h1 class="hero-title display abs">Meat Lovers Unite<br>Discover The Best Cuts</h1>
<p class="hero-text abs">Lorem ipsum odor amet, consectetuer adipiscing elit. Platea pulvinar lobortis fames, maecenas feugiat morbi venenatis. Tristique fusce vitae nibh eleifend</p>
<a class="btn" style="left:63px;top:468px;width:155px;height:45px">Order now</a>
<div class="dots abs" style="left:568px;top:580px"><span class="on"></span><span></span><span></span></div>

<section>
  <div class="about-ring abs"></div>
  <div class="about-ring-2 abs"></div>
  <div class="about-block abs"></div>
  <div class="about-card abs"><div class="ph" role="img" aria-label="Stack of raw marbled steaks with rosemary"></div></div>
  <h2 class="section-title display abs" style="left:63px;top:670px">About Us</h2>
  <p class="about-sub abs">Lorem ipsum odor amet, consectetuer adipiscing</p>
  <p class="about-text abs">Lorem ipsum odor amet, consectetuer adipiscing elit. Platea pulvinar lobortis fames, maecenas feugiat morbi venenatis. Tristique fusce vitae nibh eleifend aliquet netus lectus.&nbsp; Duis mus cursus in magnis dictumst cursus.</p>
  <a class="btn" style="left:63px;top:940px;width:155px;height:45px">Read More</a>
</section>

<section>
  <h2 class="section-title display abs" style="left:63px;top:1152px">Special Offers</h2>
  <div class="offer-box abs">
    <div class="offer-row"><span>Chuck</span><i>----------</i><span>$4.5/KG</span></div>
    <div class="offer-row"><span>Rib</span><i>----------</i><span>$5.5/KG</span></div>
    <div class="offer-row"><span>Round</span><i>----------</i><span>$6.5/KG</span></div>
    <div class="offer-row"><span>Flank</span><i>----------</i><span>$7.5/KG</span></div>
    <div class="dots" style="position:absolute;left:118px;top:206px"><span class="on"></span><span></span><span></span></div>
    <svg class="abs" style="left:215px;top:222px" width="60" height="26" viewBox="0 0 60 26" fill="none" stroke="#fff" stroke-width="1.6">
      <circle cx="12" cy="13" r="11"/><path d="M14 8l-5 5 5 5"/>
      <circle cx="46" cy="13" r="11"/><path d="M44 8l5 5-5 5"/>
    </svg>
  </div>
  <div class="badge abs"><div style="font-size:17px;font-weight:600">Up To</div><div style="font-size:33px;line-height:38px">60%</div></div>
  <div class="cow abs" role="img" aria-label="Steer silhouette chart marking chuck, rib, loin, sirloin, round, brisket, plate and flank cuts"></div>
</section>

<section>
  <svg class="boxes-band abs" viewBox="0 0 1200 556" preserveAspectRatio="none" aria-hidden="true">
    <polygon points="0,0 1200,0 1200,555 600,500 0,555" fill="#4a1905"/>
  </svg>
  <h2 class="display abs" style="left:0;top:1540px;width:1200px;text-align:center;color:var(--tan);font-size:40px">Meat Boxes</h2>
  <p class="abs" style="left:0;top:1600px;width:1200px;text-align:center;color:var(--white);font-size:19px">Order Meat Boxes To Be Free Delivered Your Home</p>
  <div class="circle-img abs" style="left:97px;top:1642px;background:radial-gradient(ellipse 45% 30% at 50% 50%,#c0304a 0%,#a8232f 70%,#f3e6e2 100%)" role="img" aria-label="Raw brisket slab"></div>
  <div class="circle-img abs" style="left:360px;top:1642px;background:radial-gradient(ellipse 42% 34% at 50% 50%,#8e2a36 0%,#6e1620 55%,#9a9a9a 75%,#ececec 100%)" role="img" aria-label="Sliced rib meat on a tray"></div>
  <div class="circle-img abs" style="left:622px;top:1642px;background:radial-gradient(ellipse 40% 30% at 50% 50%,#b02636 0%,#a8232f 55%,#c9ccd2 78%,#ffffff 100%)" role="img" aria-label="Plate cut in a sealed pack"></div>
  <div class="circle-img abs" style="left:885px;top:1642px;background:radial-gradient(ellipse 42% 28% at 50% 50%,#e0a0a6 0%,#c66a74 50%,#2a2a2a 72%,#ffffff 90%)" role="img" aria-label="Flank steaks in a tray"></div>
  <div class="label-light abs" style="left:76px;top:1875px">Brisket</div>
  <div class="label-light abs" style="left:339px;top:1875px">Rib</div>
  <div class="label-light abs" style="left:601px;top:1875px">Plate</div>
  <div class="label-light abs" style="left:864px;top:1875px">Flank</div>
  <a class="btn" style="left:523px;top:1951px;width:155px;height:47px">View More</a>
</section>

<section>
  <svg class="abs" style="left:0;top:2180px" width="1200" height="30" aria-hidden="true">
    <line x1="280" y1="15" x2="920" y2="15" stroke="#9b3a10" stroke-width="5"/>
    <circle cx="417" cy="15" r="12" fill="#d9a766"/>
    <circle cx="804" cy="15" r="12" fill="#d9a766"/>
  </svg>
  <div class="step abs" style="left:122px;top:2111px">
    <svg width="70" height="70" viewBox="0 0 70 70" fill="none" stroke="#fff" stroke-width="6"><path d="M10 6l10 12h30l10-12M14 18v46h42V18M25 34h20"/></svg>
  </div>
  <div class="step outline abs" style="left:544px;top:2111px">
    <svg width="90" height="70" viewBox="0 0 90 70"><g fill="#1e1e1e"><rect x="22" y="8" width="40" height="38" rx="3"/><path d="M62 20h14l10 14v12H62z"/><circle cx="36" cy="52" r="9"/><circle cx="72" cy="52" r="9"/><rect x="4" y="16" width="14" height="4"/><rect x="0" y="26" width="18" height="4"/><rect x="6" y="36" width="12" height="4"/></g><circle cx="36" cy="52" r="4" fill="#fff"/><circle cx="72" cy="52" r="4" fill="#fff"/></svg>
  </div>
  <div class="step abs" style="left:910px;top:2111px">
    <svg width="76" height="76" viewBox="0 0 76 76" fill="none" stroke="#fff" stroke-width="5" stroke-linejoin="round"><path d="M38 6l28 14v22M38 6L10 20v34l28 14M10 20l28 14 28-14M38 34v34M24 13l28 14"/><path d="M48 60l7 7 14-14"/></svg>
  </div>
  <div class="step-label abs" style="left:106px;top:2290px">Order</div>
  <div class="step-label abs" style="left:528px;top:2290px">Shipping</div>
  <div class="step-label abs" style="left:894px;top:2290px">Delivery</div>
</section>

<section>
  <h2 class="section-title display abs" style="left:0;top:2394px;width:1200px;text-align:center">Recipes</h2>
  <div class="recipe abs" style="left:94px;top:2488px"><div class="ph" role="img" aria-label="Mongolian beef stir fry" style="background:radial-gradient(#6b4a22,#2b1a0e)"></div></div>
  <div class="abs" style="left:94px;top:2588px;width:224px;text-align:center;color:#fff;font-size:18px;font-weight:600;letter-spacing:1.5px">Order Now</div>
  <div class="recipe abs" style="left:357px;top:2488px"><div class="ph" role="img" aria-label="Glazed BBQ beef ribs in a bowl" style="background:radial-gradient(#8a1f1a,#2a120e)"></div></div>
  <div class="recipe abs" style="left:619px;top:2488px"><div class="ph" role="img" aria-label="Spicy beef chili in a pan" style="background:radial-gradient(#9a4b22,#2a1a14)"></div></div>
  <div class="recipe abs" style="left:882px;top:2488px"><div class="ph" role="img" aria-label="Beef wellington with sauce" style="background:radial-gradient(#b5642a,#4a2412)"></div></div>
  <div class="recipe-label abs" style="left:76px;top:2726px">Mongolian Beef</div>
  <div class="recipe-label abs" style="left:339px;top:2726px">BBQ Beef Ribs</div>
  <div class="recipe-label abs" style="left:601px;top:2726px">Spicy Beef Chili</div>
  <div class="recipe-label abs" style="left:864px;top:2728px">Beef Wellington</div>

  <div class="recipe abs" style="left:94px;top:2795px"><div class="ph" role="img" aria-label="Spicy beef chili with lettuce and tomatoes" style="background:radial-gradient(#7a3a1e,#2a1a10)"></div></div>
  <div class="recipe abs" style="left:357px;top:2795px"><div class="ph" role="img" aria-label="Cottage pie beef stew" style="background:radial-gradient(#b0442a,#4a1a10)"></div></div>
  <div class="recipe abs" style="left:619px;top:2795px"><div class="ph" role="img" aria-label="Beef burger" style="background:radial-gradient(#b07a3a,#1e1a18)"></div></div>
  <div class="recipe abs" style="left:882px;top:2795px"><div class="ph" role="img" aria-label="Grilled garlic butter steak" style="background:radial-gradient(#6a3a22,#1e1410)"></div></div>
  <div class="recipe-label abs" style="left:76px;top:3042px">Spicy Beef Chili</div>
  <div class="recipe-label abs" style="left:339px;top:3042px">Cottage Pie</div>
  <div class="recipe-label abs" style="left:601px;top:3042px">Burger</div>
  <div class="recipe-label abs" style="left:864px;top:3042px">Grilled Garlic Butter<br>Steak</div>
  <a class="btn" style="left:496px;top:3124px;width:209px;height:46px">View All Recipes</a>
</section>

<section>
  <div class="contact-bg abs" role="img" aria-label="Cattle grazing on a green mountain pasture with forest behind"></div>
  <div class="contact-card abs"></div>
  <h2 class="display abs" style="left:281px;top:3278px;width:635px;text-align:center;color:var(--white);font-size:38px">Get In Touch</h2>
  <div class="field" style="left:330px;top:3341px;width:264px;height:45px">First Name</div>
  <div class="field" style="left:607px;top:3341px;width:263px;height:45px">Last Name</div>
  <div class="field" style="left:330px;top:3400px;width:540px;height:46px">Email Address</div>
  <div class="field" style="left:330px;top:3460px;width:540px;height:45px">Phone</div>
  <div class="field" style="left:330px;top:3519px;width:540px;height:96px">Leave message</div>
  <a class="btn" style="left:523px;top:3630px;width:155px;height:44px">Submit</a>
</section>

<footer class="footer abs">
  <div class="abs" style="left:63px;top:60px;color:var(--white);font-family:'Oswald',sans-serif;font-weight:600;font-size:32px;line-height:36px;text-transform:uppercase;text-align:center">Larkin Ridge<br>Provisions Co</div>
  <p class="abs" style="left:63px;top:177px;width:300px;color:var(--white);font-size:15px;line-height:20px">Lorem ipsum odor amet, consectetuer adipiscing elit. Platea pulvinar lobortis fames, maecenas feugiat</p>

  <div class="foot-h abs" style="left:430px;top:50px">Information</div>
  <div class="foot-link abs" style="left:430px;top:94px">Home</div>
  <div class="foot-link abs" style="left:430px;top:131px">About Us</div>
  <div class="foot-link abs" style="left:430px;top:169px">Meat Boxes</div>
  <div class="foot-link abs" style="left:430px;top:207px">Recipes</div>

  <div class="foot-h abs" style="left:634px;top:50px">Contact Us</div>
  <svg class="abs" style="left:634px;top:100px" width="22" height="24" viewBox="0 0 24 24" fill="#fff"><path d="M6.6 10.8a15 15 0 006.6 6.6l2.2-2.2a1 1 0 011-.25 11.4 11.4 0 003.6.57 1 1 0 011 1V20a1 1 0 01-1 1A17 17 0 013 4a1 1 0 011-1h3.5a1 1 0 011 1c0 1.25.2 2.45.57 3.57a1 1 0 01-.25 1z"/></svg>
  <div class="foot-link abs" style="left:673px;top:101px">555 014 2290</div>
  <svg class="abs" style="left:634px;top:150px" width="22" height="28" viewBox="0 0 24 30" fill="#fff"><path d="M12 0a10 10 0 00-10 10c0 8 10 20 10 20s10-12 10-20A10 10 0 0012 0zm0 14a4 4 0 110-8 4 4 0 010 8z"/></svg>
  <div class="abs" style="left:673px;top:143px;width:200px;color:var(--white);font-size:15px;line-height:20px">No2,&nbsp; aliquet netus lectus. Duis mus cursus</div>
  <svg class="abs" style="left:634px;top:209px" width="22" height="17" viewBox="0 0 22 17" fill="#fff"><rect width="22" height="17" rx="2"/><path d="M1 2l10 8 10-8" stroke="#1f0d05" stroke-width="2" fill="none"/></svg>
  <div class="foot-link abs" style="left:665px;top:204px">orders@larkinridgeco.com</div>

  <div class="foot-h abs" style="left:932px;top:50px">Follow Us</div>
  <span class="abs" style="left:934px;top:98px;width:18px;height:18px;border-radius:50%;border:2px solid #fff"></span>
  <div class="foot-link abs" style="left:966px;top:94px">Facepage</div>
  <span class="abs" style="left:934px;top:138px;width:18px;height:18px;border-radius:50%;border:2px solid #fff"></span>
  <div class="foot-link abs" style="left:966px;top:134px">Photogram</div>
  <span class="abs" style="left:934px;top:179px;width:18px;height:18px;border-radius:50%;border:2px solid #fff"></span>
  <div class="foot-link abs" style="left:966px;top:175px">Chirper</div>
</footer>
<div class="copy abs">2024 All Rights Reserved | Larkin Ridge Provisions Co</div>

</body>
</html>
```